Wagely Allies Business Card Design

We need a business card designed around our new logo. The business card should be modern in design & should communicate success, confidence, power, sophistication. The target market is young business professionals. This is for a human resource & payroll outsourcing business.

```html
<!DOCTYPE html>
<html lang="en">
<head>
<meta charset="utf-8">
<title>Wagely Allies Business Card</title>
<link rel="stylesheet" href="https://fonts.googleapis.com/css2?family=Playfair+Display:ital,wght@0,400;0,700;1,400&display=swap">
<style>
  :root {
    --backdrop: #2b2b2b;
    --card: #bfbebe;
    --card-light: #c9c8c8;
    --cap: #f0f0f0;
    --ink: #111111;
    --ink-soft: #333333;
    --rule: #7a7a7a;
    --icon-bg: #f4f4f4;
  }
  * { margin: 0; padding: 0; box-sizing: border-box; }
  html, body { width: 1200px; height: 1108px; overflow: hidden; }
  body {
    background: var(--backdrop);
    font-family: "Playfair Display", Georgia, serif;
    color: var(--ink);
    position: relative;
  }
  .card {
    position: absolute;
    top: 254px;
    width: 360px;
    height: 600px;
    border-radius: 26px;
    background: var(--card);
    overflow: hidden;
  }
  .card--front { left: 180px; }
  .card--back { left: 660px; background: var(--card-light); }
  .card__shape { position: absolute; inset: 0; width: 100%; height: 100%; }
  .wordmark {
    position: absolute;
    left: 0; right: 0;
    display: flex;
    align-items: center;
    justify-content: center;
    gap: 10px;
    font-weight: 700;
    font-size: 40px;
    letter-spacing: 0.5px;
    color: var(--ink);
  }
  .wordmark__dot {
    width: 12px; height: 12px; border-radius: 50%;
    background: #d4161b;
  }
  .card--front .wordmark { top: 96px; }
  .person { position: absolute; top: 340px; left: 0; right: 0; text-align: center; }
  .person__name { font-style: italic; font-size: 30px; }
  .person__title { font-style: italic; font-size: 17px; color: var(--ink-soft); margin-top: 2px; }
  .icons { position: absolute; top: 430px; left: 0; right: 0; display: flex; justify-content: center; gap: 8px; }
  .icons__item {
    width: 24px; height: 24px; border-radius: 4px;
    background: var(--icon-bg);
    display: flex; align-items: center; justify-content: center;
  }
  .contact {
    position: absolute; top: 466px; left: 0; right: 0;
    text-align: center; font-size: 17px; line-height: 21px;
  }
  .rule { position: absolute; top: 556px; left: 60px; right: 60px; height: 1px; background: var(--rule); }
  .address {
    position: absolute; top: 562px; left: 0; right: 0;
    text-align: center; font-size: 16px; line-height: 19px; color: var(--ink-soft);
  }
  .card--front .address { top: 564px; font-size: 14px; line-height: 16px; }
  .card--back .wordmark { top: 420px; }
  .site { position: absolute; top: 484px; left: 0; right: 0; text-align: center; font-size: 19px; letter-spacing: 1px; }
</style>
</head>
<body>
  <section class="card card--front" aria-label="Card front">
    <svg class="card__shape" viewBox="0 0 360 600" aria-hidden="true">
      <path d="M0 0 H360 V40 C340 250 260 318 180 318 C100 318 20 250 0 40 Z" fill="#f0f0f0"/>
      <path d="M0 220 C40 420 160 520 360 600 L360 600 L0 600 Z" fill="#c6c5c5" opacity="0.6"/>
    </svg>
    <div class="wordmark"><span class="wordmark__dot"></span>Wagely Allies</div>
    <div class="person">
      <div class="person__name">Dorian Vale</div>
      <div class="person__title">Managing Director</div>
    </div>
    <div class="icons">
      <span class="icons__item"><svg width="14" height="14" viewBox="0 0 14 14"><path d="M2 4 Q7 0 12 4 L11 6 L9 5 L9 4 Q7 3 5 4 L5 5 L3 6 Z M3 7 H11 L12 12 H2 Z" fill="#222"/></svg></span>
      <span class="icons__item"><svg width="14" height="14" viewBox="0 0 14 14"><rect x="4" y="1" width="6" height="12" rx="1" fill="none" stroke="#222" stroke-width="1.5"/></svg></span>
      <span class="icons__item"><svg width="14" height="14" viewBox="0 0 14 14"><rect x="1" y="3" width="12" height="8" fill="#222"/><path d="M1 3 L7 8 L13 3" fill="none" stroke="#f4f4f4" stroke-width="1"/></svg></span>
      <span class="icons__item"><svg width="14" height="14" viewBox="0 0 14 14"><circle cx="7" cy="7" r="6" fill="#222"/><path d="M1 7 H13 M7 1 C4 4 4 10 7 13 M7 1 C10 4 10 10 7 13" stroke="#f4f4f4" stroke-width="0.8" fill="none"/></svg></span>
    </div>
    <div class="contact">
      444 555 7210<br>444 555 7210<br>hello@wagelyallies.com<br>www.wagelyallies.com
    </div>
    <div class="rule"></div>
    <div class="address">58, Harbor Row<br>Northvale, 30917</div>
  </section>

  <section class="card card--back" aria-label="Card back">
    <svg class="card__shape" viewBox="0 0 360 600" aria-hidden="true">
      <path d="M0 100 C60 380 200 520 360 560 L360 600 L0 600 Z" fill="#c2c1c1" opacity="0.7"/>
    </svg>
    <div class="wordmark"><span class="wordmark__dot"></span>Wagely Allies</div>
    <div class="site">www.wagelyallies.com</div>
  </section>
</body>
</html>
```